Site refresh

Our current site is completely static which is no longer appropriate for us. We're looking for a more minimalist design, responsive theme that conveys a professional and dynamic organisation. We need a much more interactive site in order to educate potential customers, capture their information and deliver white papers we are writing. Quite simply the site needs to 'sell' the prospect the idea that they really must talk to us.
We are an IT consultancy specialising in Big Data and process driven IT in order to make organisations more effective, save money and outstrip their competition. Some of our clients include insurance, logistics and professional services organisations.
The final design needs to utilise small elements of orange and black. The current site can be found at www.brackenloftit.co.uk and a test Wordpress page can be found at bigdata.brackenloftit.co.uk.
Reason: Sorry, I've been off for half-term with the kids so not had chance to review the designs.

```html
<!DOCTYPE html>
<html lang="en">
<head>
<meta charset="utf-8">
<title>BrackenloftIT – IT Consultancy</title>
<link href="https://fonts.googleapis.com/css2?family=Open+Sans:wght@300;400;600;700&family=Ubuntu:wght@300;400;500;700&display=swap" rel="stylesheet">
<style>
:root{
  --orange:#f07b16;
  --orange-deep:#e86f0c;
  --header:#3b3b3b;
  --ink:#333;
  --muted:#6d6d6d;
  --footer:#2b2b2b;
  --footer-base:#232323;
  --white:#fff;
  --page:#fafafa;
}
*{margin:0;padding:0;box-sizing:border-box}
html,body{width:1200px;height:2206px;overflow:hidden}
body{font-family:"Open Sans",Arial,sans-serif;color:var(--ink);background:var(--white);position:relative}
.site-header{position:absolute;top:0;left:0;width:1200px;height:106px;background:var(--header)}
.brand{position:absolute;left:88px;top:30px;font-family:"Ubuntu",sans-serif;font-weight:700;font-size:34px;color:var(--white);letter-spacing:-1px}
.main-nav a{position:absolute;top:52px;font-size:16px;color:var(--white);text-decoration:none}
.main-nav .active::after{content:"";position:absolute;left:-13px;right:-13px;top:44px;height:6px;background:var(--orange)}
.hero{position:absolute;top:106px;left:0;width:1200px;height:469px;background:linear-gradient(100deg,#1c1c1c 0%,#2a2622 30%,#151515 60%,#262626 100%)}
.hero-copy{position:absolute;left:85px;top:128px;color:var(--white)}
.hero-kicker{font-family:"Ubuntu",sans-serif;font-size:35px;font-weight:400}
.hero-title{font-family:"Ubuntu",sans-serif;font-size:48px;font-weight:400;margin-top:-4px}
.hero-text{font-size:14px;color:#cfcfcf;line-height:24px;margin-top:4px}
.hero-dots{position:absolute;left:566px;top:440px;display:flex;gap:8px}
.hero-dots span{width:11px;height:11px;border-radius:50%;background:#555}
.hero-dots span:first-child{background:#222}
.intro{position:absolute;top:575px;left:0;width:1200px;height:323px;text-align:center}
.intro h1{font-family:"Ubuntu",sans-serif;font-weight:300;font-size:36px;color:#333;margin-top:48px}
.intro p{width:1028px;margin:0 auto;font-size:12.6px;line-height:24px;color:var(--muted)}
.intro p:first-of-type{margin-top:12px}
.intro p+p{margin-top:11px}
.services{position:absolute;top:898px;left:0;width:1200px;height:424px;background:var(--orange);color:var(--white);text-align:center}
.services h2{font-family:"Ubuntu",sans-serif;font-weight:300;font-size:34px;margin-top:42px}
.services .lead{font-size:13.5px;margin-top:4px;color:#ffe4cc}
.service{position:absolute;top:160px;width:240px;text-align:center}
.service svg{display:block;margin:0 auto}
.service h3{font-family:"Ubuntu",sans-serif;font-weight:400;font-size:24px;margin-top:10px}
.service p{font-size:12.5px;line-height:22px;margin-top:6px;color:#ffe9d6}
.features{position:absolute;top:1322px;left:0;width:1200px;height:501px;background:var(--page)}
.feature{position:absolute;top:63px;width:328px}
.feature-media{height:135px}
.feature h3{font-family:"Ubuntu",sans-serif;font-weight:400;font-size:24px;color:#444;margin:16px 0 0 4px}
.feature p{font-size:12.5px;line-height:24.5px;color:var(--muted);margin:8px 0 0 4px}
.btn{display:inline-block;margin:12px 0 0 4px;width:113px;height:36px;line-height:36px;text-align:center;background:#2b2b2b;color:var(--white);font-size:13px;font-weight:600;border-radius:3px;box-shadow:0 2px 0 #111}
.site-footer{position:absolute;top:1823px;left:0;width:1200px;height:315px;background:var(--footer);border-top:5px solid #1c1c1c}
.footer-col{position:absolute;top:42px}
.footer-col h4{font-family:"Ubuntu",sans-serif;font-weight:500;font-size:20px;color:var(--orange);margin-bottom:6px}
.footer-col li{list-style:none;font-size:12.8px;color:#e2e2e2;line-height:27.3px}
.footer-base{position:absolute;top:2138px;left:0;width:1200px;height:68px;background:var(--footer-base)}
.copyright{position:absolute;left:85px;top:25px;font-size:12px;color:#bbb}
.social{position:absolute;left:1021px;top:18px;display:flex;gap:5px}
.social span{width:29px;height:29px;border-radius:50%;background:var(--white)}
</style>
</head>
<body>
<header class="site-header">
  <div class="brand">brackenloftit</div>
  <nav class="main-nav">
    <a class="active" style="left:513px">Home</a>
    <a style="left:598px">About Us</a>
    <a style="left:707px">Services</a>
    <a style="left:809px">Solutions</a>
    <a style="left:919px">Case Studies</a>
    <a style="left:1056px">Contact</a>
  </nav>
</header>

<section class="hero" role="img" aria-label="Photo of a black keyboard with orange-lit keys beside a leather notebook and fountain pen">
  <div class="hero-copy">
    <div class="hero-kicker">Etiam eu urna Sed porta</div>
    <div class="hero-title">Phasellus dolor scelerisque</div>
    <div class="hero-text">Lorem ipsum dolor sit amet consectetur adipiscing elit Nam cursus<br>Morbi ut mi Nullam enim leo egesta</div>
  </div>
  <div class="hero-dots"><span></span><span></span><span></span><span></span></div>
</section>

<section class="intro">
  <h1>It’s time for some clear thinking and fresh approach</h1>
  <p>BrackenloftIT is a business change and technology consultancy passionate about improving the way you work. Our enablers are the very latest solutions from the most trusted names in Information Technology and Communications brought to life by a dedicated team of professionals.</p>
  <p>The objective is to simplify your business environment into an intuitive user friendly one where owners and senior managers have an understanding of their IT eco-system and are comfortable that it is supporting the business in the way they want it to. It is our ambition to remove the mystery that surrounds IT and Communications so you have a clear understanding of what you are purchasing, why you are purchasing it and what benefits it will bring you. The first step is to gain a close understanding of your business, then at a pace that suits you, migrate to an environment where your information will never be lost, is totally secure and can be accessed anywhere.</p>
</section>

<section class="services">
  <h2>SERVICES WE PROVIDE</h2>
  <p class="lead">Aliquam nec erat at purus cursus interdum Vestibulum ligula augue bibendum accumsan vestibulum ut commodo a mi Morbi ornare gravida</p>

  <div class="service" style="left:93px">
    <svg width="80" height="84" viewBox="0 0 80 84" fill="none" stroke="#fff" stroke-width="6"><circle cx="34" cy="34" r="24"/><line x1="52" y1="52" x2="74" y2="76" stroke-linecap="round" stroke-width="9"/></svg>
    <h3>Discover</h3>
    <p>Morbi diam mauris viverra in gravida<br>eu mattis in ante Morbi egetarcu<br>Morbi porta ullamcorper</p>
  </div>
  <div class="service" style="left:346px">
    <svg width="80" height="84" viewBox="0 0 80 84" fill="#fff"><path d="M8 38 Q10 18 34 18 H54 V6 L76 26 L54 46 V34 H34 Q20 34 8 38Z"/><path d="M72 46 Q70 66 46 66 H26 V78 L4 58 L26 38 V50 H46 Q60 50 72 46Z"/></svg>
    <h3>Transform</h3>
    <p>Morbi diam mauris viverra in gravida<br>eu mattis in ante Morbi egetarcu<br>Morbi porta ullamcorper</p>
  </div>
  <div class="service" style="left:600px">
    <svg width="80" height="84" viewBox="0 0 80 84"><circle cx="40" cy="36" r="32" fill="#fff"/><circle cx="40" cy="36" r="20" fill="var(--orange)"/><path d="M20 62 L10 80 L24 76 L30 84 L38 66Z M60 62 L70 80 L56 76 L50 84 L42 66Z" fill="#fff"/><text x="40" y="45" text-anchor="middle" font-family="Ubuntu,sans-serif" font-size="26" font-weight="700" fill="#fff">1</text></svg>
    <h3>Results</h3>
    <p>Morbi diam mauris viverra in gravida<br>eu mattis in ante Morbi egetarcu<br>Morbi porta ullamcorper</p>
  </div>
  <div class="service" style="left:856px">
    <svg width="80" height="84" viewBox="0 0 80 84" fill="none" stroke="#fff" stroke-width="6"><path d="M12 46 V38 A28 28 0 0 1 68 38 V46"/><rect x="6" y="40" width="14" height="24" rx="5" fill="#fff"/><rect x="60" y="40" width="14" height="24" rx="5" fill="#fff"/><path d="M66 64 Q66 76 48 76" stroke-width="4"/></svg>
    <h3>Support</h3>
    <p>Morbi diam mauris viverra in gravida<br>eu mattis in ante Morbi egetarcu<br>Morbi porta ullamcorper</p>
  </div>
</section>

<section class="features">
  <article class="feature" style="left:82px">
    <div class="feature-media" role="img" aria-label="Product banner for a cloud device management service" style="background:linear-gradient(180deg,#3c72b8,#2a5a9c)"></div>
    <h3>Cloud Device Manager</h3>
    <p>Users depend on their PCs, with Device Manager© simply manage and secure PCs using desktop™ cloud services. Device Manager is an integrated solution delivering cloud-based management and security through a single Web console.</p>
    <a class="btn">READ MORE</a>
  </article>
  <article class="feature" style="left:436px">
    <div class="feature-media" role="img" aria-label="Photo of cupped hands holding a green glass globe" style="background:radial-gradient(circle at 50% 40%,#6aa84f 0,#c9b08d 35%,#e8d3b8 70%)"></div>
    <h3>Environment</h3>
    <p>Users depend on their PCs, with Device Manager© simply manage and secure PCs using desktop™ cloud services. Device Manager is an integrated solution delivering cloud-based management and security through a single Web console.</p>
    <a class="btn">READ MORE</a>
  </article>
  <article class="feature" style="left:791px">
    <div class="feature-media" role="img" aria-label="Product banner for a hosted office software suite" style="background:#fff;border:1px solid #ccc"></div>
    <h3>Hosted Office Suite</h3>
    <p>Users depend on their PCs, with Device Manager© simply manage and secure PCs using desktop™ cloud services. Device Manager is an integrated solution delivering cloud-based management and security through a single Web console.</p>
    <a class="btn">READ MORE</a>
  </article>
</section>

<footer class="site-footer">
  <div class="footer-col" style="left:94px"><h4>Cloud &amp; Business Solutions</h4><ul><li>Hosted Cloud Services</li><li>Enterprise Mail Services</li><li>Managed Cloud</li><li>Public Cloud Services</li><li>Business Intelligence</li><li>Customer Relationships</li><li>Efficiency</li></ul></div>
  <div class="footer-col" style="left:412px"><h4>Services</h4><ul><li>Innovation</li><li>Cost Control</li><li>Consultancy</li><li>Achievment of Result</li><li>Analysis</li><li>Compliance</li><li>Secure Disposal</li></ul></div>
  <div class="footer-col" style="left:604px"><h4>About Us</h4><ul><li>Testimonials</li><li>Help and advice</li><li>Brackenloft IT Blog</li><li>Question &amp; Answers</li><li>Resources</li></ul></div>
  <div class="footer-col" style="left:802px"><h4>Support</h4><ul><li>Term of Services</li><li>Privacy Policy</li><li>Contact Us</li><li>Sitemap</li><li>Security</li></ul></div>
  <div class="footer-col" style="left:982px"><h4>Infrastructure</h4><ul><li>Wide area Network</li><li>Data Centre</li><li>Security</li><li>Telephony</li></ul></div>
</footer>
<div class="footer-base">
  <div class="copyright">© 2014 Company Name &nbsp;All right reserved &nbsp;Term of Use</div>
  <div class="social"><span></span><span></span><span></span></div>
</div>
</body>
</html>
```